Paint Protection Options

This is a flyer that will describe two different paint protection options for vehicles. I have mocked up a Word doc. As well, I've included some samples of other flyers where I like the "look". I am not locked into any single layout or design. In my Word doc I have them side-by-side. I think that makes sense but open to ideas. I've also added some pics of the two options being applied to cars. We need to have one of each (ceramic and ppf) at a minimum. In the grid I'm thinking different colors dots/circles to differentiate the different levels. But again, I'm open to suggestions. You can use the symbol for microns in the grid under the Thickness row. I spelled it out because I didn't know how to insert.

```html
<!DOCTYPE html>
<html lang="en">
<head>
<meta charset="utf-8">
<title>Paint Protection Options for Vehicles</title>
<link href="https://fonts.googleapis.com/css2?family=Poppins:wght@400;500;600;700;800&display=swap" rel="stylesheet">
<style>
:root{
  --navy:#0b3e62;
  --blue:#0a7cc1;
  --blue-mid:#1a6fa6;
  --charcoal:#2a2a2a;
  --ink:#2c2c2c;
  --grey-head:#d4d6d9;
  --grey-row:#eef1f4;
  --line:#9aa0a6;
  --green:#0c9c4a;
  --yellow:#f1e400;
  --red:#e10c14;
  --white:#ffffff;
}
*{box-sizing:border-box;margin:0;padding:0}
html,body{width:993px;height:1200px;overflow:hidden;background:var(--white)}
body{font-family:"Poppins",sans-serif;color:var(--ink)}
.flyer{position:relative;width:993px;height:1200px;background:var(--white)}

/* header */
.hero{position:absolute;left:0;top:0;width:993px;height:245px}
.hero svg{position:absolute;inset:0}
.hero-title{position:absolute;left:150px;top:30px;width:250px;text-align:center;color:var(--white);font-weight:800;line-height:.92}
.hero-title .big{display:block;font-size:66px;letter-spacing:1px}
.hero-title .mid{display:block;font-size:43px;margin-top:4px}
.hero-sub{position:absolute;left:130px;top:198px;color:var(--white);font-weight:800;font-size:36px;letter-spacing:.5px}

/* option panels */
.option{position:absolute;top:264px;width:409px;height:445px;border:1.5px solid var(--charcoal);background:var(--white)}
.option-ceramic{left:88px}
.option-ppf{left:497px;border-color:var(--navy)}
.option-head{height:50px;display:flex;align-items:center;justify-content:center;color:var(--white);font-weight:700;font-size:23px}
.option-ceramic .option-head{background:var(--charcoal);border-radius:0 14px 0 0}
.option-ppf .option-head{background:var(--navy);border-radius:14px 0 0 0}
.option-body{padding:10px 12px 0 13px;font-size:11.2px;line-height:13.8px;text-align:justify;height:278px}
.option-body p{margin-bottom:8px}
.benefits{list-style:none;margin-top:13px}
.benefits li{position:relative;padding-left:20px;color:var(--blue);font-weight:600;font-size:11.4px;line-height:15px;text-align:left}
.benefits svg{position:absolute;left:0;top:3px;width:10px;height:10px}
.option-photo{position:absolute;left:0;right:0;bottom:0;height:146px}
.option-ceramic .option-photo{background:linear-gradient(120deg,#0d1d33,#1c3b63 45%,#3e7fc7 70%,#0f2440)}
.option-ppf .option-photo{background:linear-gradient(110deg,#b8121c,#d9485a 40%,#d6d0cc 70%,#2a2f38)}

/* comparison table */
.compare-title{position:absolute;left:0;width:993px;top:720px;text-align:center;color:var(--navy);font-weight:800;font-size:31px}
.compare{position:absolute;left:84px;top:755px;width:827px;border-collapse:collapse;table-layout:fixed;font-size:12px}
.compare col.c-feat{width:219px}
.compare col.c-opt{width:203px}
.compare th,.compare td{border:1px solid var(--line);height:27px;text-align:center;vertical-align:middle}
.compare thead th{height:50px;font-weight:700;font-size:13px;line-height:13px}
.compare thead th.feat{background:transparent;border:none;vertical-align:bottom;padding:0}
.feat-label{display:block;background:var(--grey-head);border:1px solid var(--line);height:28px;line-height:28px;font-size:13px}
.compare thead th.wax{background:var(--navy);color:var(--white)}
.compare thead th.other{background:var(--grey-head);color:#444;text-align:left}
.th-inner{display:flex;align-items:center;gap:12px;padding-left:18px}
.th-inner svg{width:30px;height:26px;flex:none}
.compare tbody th{font-weight:600;font-size:12px;color:#333;background:var(--white)}
.compare tbody tr:nth-child(even) th,.compare tbody tr:nth-child(even) td{background:var(--grey-row)}
.compare tbody td.wax,.compare tbody tr:nth-child(even) td.wax{background:var(--blue);color:var(--white)}
.compare td.val{text-align:left;padding-left:26px;font-size:12px;color:#444}
.compare td.wax.val{text-align:center;padding-left:0;color:var(--white)}
.dot{display:inline-block;width:9px;height:9px;border-radius:50%;vertical-align:middle}
.full{background:var(--green)}
.ring{background:var(--green);box-shadow:0 0 0 1px var(--white) inset;border:1px solid var(--white)}
.half{background:linear-gradient(90deg,var(--yellow) 50%,var(--white) 50%);border:1px solid var(--yellow)}
.quarter{background:conic-gradient(var(--yellow) 0 25%,var(--white) 25% 100%);border:1px solid #d8c800}
.three{background:conic-gradient(var(--white) 0 25%,var(--green) 25% 100%);border:1px solid var(--green)}
.low-q{background:conic-gradient(var(--yellow) 0 25%,var(--white) 25% 100%);border:1px solid #d8c800}
.bad{background:var(--red)}
.level{font-weight:700;font-size:12.5px}
.level-low{background:linear-gradient(90deg,#ffff00,#e3db00) !important;color:#333}
.level-med{background:linear-gradient(90deg,#0aa04f,#05522a) !important;color:var(--white)}
.level-high{background:linear-gradient(90deg,#e40010,#9c0a10) !important;color:var(--white)}
</style>
</head>
<body>
<main class="flyer">

  <header class="hero">
    <svg width="993" height="245" viewBox="0 0 993 245" aria-hidden="true">
      <defs>
        <linearGradient id="heroBlue" x1="0" y1="0" x2="1" y2="1">
          <stop offset="0" stop-color="#0d5f95"/>
          <stop offset=".6" stop-color="#137ab8"/>
          <stop offset="1" stop-color="#0b4f80"/>
        </linearGradient>
      </defs>
      <rect x="0" y="0" width="520" height="245" fill="url(#heroBlue)"/>
      <polygon points="497,0 520,0 471,113 530,245 505,245 447,113" fill="var(--charcoal)"/>
      <polygon points="76,191 460,191 483,245 50,245" fill="var(--charcoal)"/>
    </svg>
    <div role="img" aria-label="Technicians applying clear protection film to a dark car hood"
         style="position:absolute;left:0;top:0;width:993px;height:245px;clip-path:polygon(520px 0,993px 0,993px 245px,530px 245px,471px 113px);background:linear-gradient(120deg,#3a4a57,#1c252e 45%,#6e7f8c 70%,#b9c4cc)"></div>
    <h1 class="hero-title"><span class="big">PAINT</span><span class="mid">PROTECTION</span><span class="mid">OPTIONS</span></h1>
    <div class="hero-sub">FOR VEHICLES</div>
  </header>

  <section class="option option-ceramic">
    <h2 class="option-head">CERAMIC COATINGS</h2>
    <div class="option-body">
      <p>Ceramic coatings are liquid polymer coatings that bond to a vehicle’s painted surface. The coatings are formulated to retain the showroom finish by protecting against corrosion and contaminants like UV damage, oxidation, road salt and acid rain. Ceramic coatings give your car a deep, glossy finish that reflects light and makes your paint look more vibrant while greatly extending the paint’s lifespan.</p>
      <p>The chemical bonding process improves color depth and leaves a smooth finish. The hydrophobic (water repellent) properties repel water and dirt as well as protect against damaging pollutants. This makes care and maintenance a breeze while retaining the show room finish. Never wax again!</p>
      <ul class="benefits">
        <li><svg viewBox="0 0 10 10"><circle cx="5" cy="5" r="4.3" fill="none" stroke="var(--blue)" stroke-width="1"/><path d="M3 5.2l1.4 1.3L7 3.8" fill="none" stroke="var(--blue)" stroke-width="1"/></svg>Enhance and retain showroom finish</li>
        <li><svg viewBox="0 0 10 10"><circle cx="5" cy="5" r="4.3" fill="none" stroke="var(--blue)" stroke-width="1"/><path d="M3 5.2l1.4 1.3L7 3.8" fill="none" stroke="var(--blue)" stroke-width="1"/></svg>Protect against corrosion and contaminants</li>
        <li><svg viewBox="0 0 10 10"><circle cx="5" cy="5" r="4.3" fill="none" stroke="var(--blue)" stroke-width="1"/><path d="M3 5.2l1.4 1.3L7 3.8" fill="none" stroke="var(--blue)" stroke-width="1"/></svg>Reduce care and maintenance</li>
      </ul>
    </div>
    <div class="option-photo" role="img" aria-label="Gloved hands applying ceramic coating to a dark car panel"></div>
  </section>

  <section class="option option-ppf">
    <h2 class="option-head">PAINT PROTECTION FILM (PPF)</h2>
    <div class="option-body">
      <p>Paint Protection Film (PPF) is a transparent, thermoplastic urethane film that is applied directly to the car’s painted surfaces. PPF excels at shielding your vehicle from rock chips, scratches, and other physical damage. It has self-healing properties that can repair minor scratches and swirl marks over time.</p>
      <p style="margin-top:12px">Every piece of PPF is custom cut to fit each panel of your vehicle and provide maximum coverage. The film protects your vehicle from scratches, rock chips, staining, corrosion, fading, chemicals, insects, and road debris. It helps keep your paint looking new, saving you money and improving your resale value.</p>
      <ul class="benefits" style="margin-top:22px">
        <li><svg viewBox="0 0 10 10"><circle cx="5" cy="5" r="4.3" fill="none" stroke="var(--blue)" stroke-width="1"/><path d="M3 5.2l1.4 1.3L7 3.8" fill="none" stroke="var(--blue)" stroke-width="1"/></svg>Protect against rock chips, scratches, and physical damage</li>
        <li><svg viewBox="0 0 10 10"><circle cx="5" cy="5" r="4.3" fill="none" stroke="var(--blue)" stroke-width="1"/><path d="M3 5.2l1.4 1.3L7 3.8" fill="none" stroke="var(--blue)" stroke-width="1"/></svg>Easily repair minor scratches and swirl marks</li>
        <li><svg viewBox="0 0 10 10"><circle cx="5" cy="5" r="4.3" fill="none" stroke="var(--blue)" stroke-width="1"/><path d="M3 5.2l1.4 1.3L7 3.8" fill="none" stroke="var(--blue)" stroke-width="1"/></svg>Protect against corrosion and contaminants</li>
      </ul>
    </div>
    <div class="option-photo" role="img" aria-label="Hands stretching clear protection film over a red car"></div>
  </section>

  <h2 class="compare-title">PAINT PROTECTION OPTIONS</h2>

  <table class="compare">
    <colgroup><col class="c-feat"><col class="c-opt"><col class="c-opt"><col class="c-opt"></colgroup>
    <thead>
      <tr>
        <th class="feat"><span class="feat-label">FEATURE</span></th>
        <th class="wax"><div class="th-inner">
          <svg viewBox="0 0 30 26" aria-hidden="true"><rect x="10" y="8" width="17" height="12" rx="3" fill="none" stroke="#cfe6f7" stroke-width="1.6"/><rect x="2" y="13" width="5" height="10" rx="1" fill="none" stroke="#cfe6f7" stroke-width="1.4"/><circle cx="14" cy="21" r="2" fill="#cfe6f7"/><circle cx="23" cy="21" r="2" fill="#cfe6f7"/></svg>
          CAR WAX</div></th>
        <th class="other"><div class="th-inner">
          <svg viewBox="0 0 30 26" aria-hidden="true"><path d="M4 16l3-6h16l3 6v6H4z" fill="none" stroke="var(--blue)" stroke-width="1.8"/><circle cx="9" cy="22" r="2" fill="var(--blue)"/><circle cx="21" cy="22" r="2" fill="var(--blue)"/><path d="M5 3l1 2 2 1-2 1-1 2-1-2-2-1 2-1z" fill="var(--blue)"/></svg>
          CERAMIC<br>COATING</div></th>
        <th class="other"><div class="th-inner">
          <svg viewBox="0 0 30 26" aria-hidden="true"><path d="M2 17l4-6h14l6 6v4H2z" fill="var(--blue)"/><circle cx="8" cy="21" r="2.4" fill="#fff" stroke="var(--blue)"/><circle cx="21" cy="21" r="2.4" fill="#fff" stroke="var(--blue)"/></svg>
          PAINT<br>PROTECTION FILM</div></th>
      </tr>
    </thead>
    <tbody>
      <tr><th>Duration</th><td class="wax val">2 - 4 Weeks</td><td class="val">3 - 10 Years</td><td class="val">7 - 10 Years</td></tr>
      <tr><th>Thickness</th><td class="wax val">1.5 - 5 µm</td><td class="val">7 - 10 µm</td><td class="val">200 - 250 µm</td></tr>
      <tr><th>Gloss Enhancement</th><td class="wax"><span class="dot ring"></span></td><td><span class="dot full"></span></td><td><span class="dot full"></span></td></tr>
      <tr><th>Acid Rain Damage</th><td class="wax"><span class="dot half"></span></td><td><span class="dot full"></span></td><td><span class="dot full"></span></td></tr>
      <tr><th>Corrosion Prevention</th><td class="wax"><span class="dot half"></span></td><td><span class="dot full"></span></td><td><span class="dot full"></span></td></tr>
      <tr><th>UV/Oxidation Protection</th><td class="wax"><span class="dot half"></span></td><td><span class="dot full"></span></td><td><span class="dot full"></span></td></tr>
      <tr><th>Hard Water Damage</th><td class="wax"><span class="dot quarter"></span></td><td><span class="dot three"></span></td><td><span class="dot full"></span></td></tr>
      <tr><th>Insect Splatter Damage</th><td class="wax"><span class="dot quarter"></span></td><td><span class="dot three"></span></td><td><span class="dot full"></span></td></tr>
      <tr><th>Chip Protection</th><td class="wax"><span class="dot bad"></span></td><td><span class="dot low-q"></span></td><td><span class="dot full"></span></td></tr>
      <tr><th>Scratch Protection</th><td class="wax"><span class="dot bad"></span></td><td><span class="dot low-q"></span></td><td><span class="dot full"></span></td></tr>
      <tr><th>Swirl Protection</th><td class="wax"><span class="dot bad"></span></td><td><span class="dot bad"></span></td><td><span class="dot full"></span></td></tr>
      <tr><th>Application Complexity</th><td class="level level-low">LOW</td><td class="level level-med">MEDIUM</td><td class="level level-high">HIGH</td></tr>
    </tbody>
  </table>

</main>
</body>
</html>
```